Organic skincare label - minimalist, earthy, luxe design needed!

I need a label design for a luxury natural skin care line called "Velka Botanix". Velka means 'earth' in Swahili. I would like the design to embody an earthy feel but be minimalistic and give a luxe vibe. My first product will be a Tumeric and Neem Scrub.

The size of the jar is 8oz, label dimensions should be (1.625" Tall x 8.5" Wide)
I will be making other products too such as; oils + toners so I feel free to do labels for glass bottles and/or spray bottles as well.

Forest green, light pinks/nudes/beige, grey, white, gold, are colors that can be used (not all have to be used).

I have included pictures of some things I've worked on myself as well as my original logo design but I need to simplify the logo, no circle around it.
Feel free to get creative.

Thank you! :)
Updates

Target Market(s)

Socially Conscious, Beauty Enthusiast, Minimalist

Industry/Entity Type

Skin Care

Font styles to use
Sans Serif
Other font styles liked:
• "Wonderlove doodle" is the font used for "Velka" in the logo. Feel free to use that or change it as you see fit.

Requirements
Must have
• Simplistic design
would like to stick to a font close to the ones in the logo. Either the one used for the name "Velka" OR the one that the slogan "ROOTED RITUALS" uses.

I have also included some pictures to capture the aesthetic of my social media and website.

Gender neutral

```html
<!DOCTYPE html>
<html lang="en">
<head>
<meta charset="utf-8">
<title>Velka Botanix – Rose Serum Label</title>
<link rel="stylesheet" href="https://fonts.googleapis.com/css2?family=Open+Sans:wght@300;400;600&family=Playfair+Display:wght@600&display=swap">
<style>
  :root {
    --label-blush: #e2d8d3;
    --divider: #ffffff;
    --ink-stone: #5d5b54;
    --ink-dark: #2a2a2a;
    --ink-grey: #6a6866;
    --copper: #ad7649;
    --frond-light: #d6cfc9;
    --frond-tan: #b49a85;
    --leaf-green: #3e5a3a;
    --skin-nude: #d9b799;
  }
  * { margin: 0; padding: 0; box-sizing: border-box; }
  html, body { width: 1200px; height: 230px; overflow: hidden; background: #ffffff; }
  .label {
    position: relative;
    width: 1200px;
    height: 230px;
    background: var(--label-blush);
    font-family: "Open Sans", Arial, sans-serif;
    overflow: hidden;
  }
  .photo { position: absolute; top: 0; height: 230px; }
  .photo--frond {
    left: 0; width: 298px;
    background: linear-gradient(120deg, var(--frond-tan) 0%, var(--frond-light) 45%, #c9b3a2 70%, var(--frond-light) 100%);
  }
  .photo--botanical {
    left: 1016px; width: 184px;
    background: linear-gradient(90deg, var(--frond-light) 0%, var(--leaf-green) 30%, var(--skin-nude) 60%, #c6a384 80%, var(--leaf-green) 100%);
  }
  .divider { position: absolute; background: var(--divider); }
  .divider--v { top: 0; width: 2px; height: 230px; }
  .divider--h { top: 113px; height: 2px; }
  .divider--h-photo { left: 0; top: 113px; width: 298px; height: 1px; opacity: .5; }
  .brand-mark { position: absolute; left: 696px; top: 30px; width: 14px; height: 14px; border-radius: 50%; background: var(--copper); }
  .brand-name {
    position: absolute; left: 676px; top: 74px;
    font-weight: 600; font-size: 17px; line-height: 1; color: var(--copper); letter-spacing: .5px;
  }
  .brand-tagline {
    position: absolute; left: 679px; top: 95px;
    font-size: 5.5px; font-weight: 600; line-height: 1; color: var(--copper); letter-spacing: .4px;
    white-space: nowrap;
  }
  .product-name {
    position: absolute; left: 505px; top: 92px;
    font-family: "Playfair Display", Georgia, serif; font-weight: 600;
    font-size: 68px; line-height: 1; color: var(--ink-stone); letter-spacing: 1px;
    white-space: nowrap;
  }
  .product-type {
    position: absolute; left: 544px; top: 165px;
    font-size: 23.5px; font-weight: 300; line-height: 1; white-space: nowrap;
  }
  .product-type .accent { color: var(--ink-dark); }
  .product-type .base { color: var(--ink-grey); }
  .product-volume {
    position: absolute; left: 570px; top: 191px;
    font-size: 12.5px; font-weight: 300; line-height: 1; color: var(--ink-dark); white-space: nowrap;
  }
  .vertical-text {
    position: absolute; writing-mode: vertical-rl; transform: rotate(180deg);
    color: var(--ink-dark); text-transform: uppercase; white-space: nowrap;
  }
  .ingredients { left: 918px; top: 44px; height: 160px; font-size: 9.5px; font-weight: 300; line-height: 13.5px; text-align: left; }
  .origin { left: 992px; top: 72px; height: 132px; font-size: 12px; font-weight: 400; line-height: 16px; }
</style>
</head>
<body>
  <main class="label">
    <div class="photo photo--frond" role="img" aria-label="Dried palm frond laid on a pale grey surface"></div>
    <div class="divider divider--h-photo"></div>

    <div class="divider divider--v" style="left:299px"></div>
    <div class="divider divider--v" style="left:599px"></div>
    <div class="divider divider--v" style="left:899px"></div>
    <div class="divider divider--h" style="left:299px; width:717px"></div>

    <span class="brand-mark"></span>
    <p class="brand-name">Velka</p>
    <p class="brand-tagline">ROOTED RITUALS</p>

    <h1 class="product-name">VELKA</h1>
    <p class="product-type"><span class="accent">ROSE</span> <span class="base">SERUM</span></p>
    <p class="product-volume">1FL OZ/ 59 ML</p>

    <p class="vertical-text ingredients">Ingredients:<br>Organic rosehip, seed<br>oil, organic pomgranate oil,<br>vitamin E non-GMO</p>
    <p class="vertical-text origin">Made in Houston, TX</p>

    <div class="photo photo--botanical" role="img" aria-label="Arm wrapped around large green tropical leaves"></div>
  </main>
</body>
</html>
```